VerdaTurfix - 11" x 4" Door Hanger, full color both sides

We need a door hanger designed, 11" x 4", full color both sides, We are a lawn care company that provides lawn mowing, and other services to clients. This door hanger will be place on the 9 neighbors of our current clients. The ad needs to state that we provided lawn service to one of their neighbors today, and that we are in their neighborhood each week on that day. The door hanger will have 4 printings, substituting the day of Tuesday, Wednesday, Thursday, and Friday. All the art work and text will remain the same except the day of the week. For information about VerdaTurfix, please visit our website www.verdaturfix.net. The main emphasis of the message should be that we are their every week on that day, and the benefits to them of using our service (ie. quality time with their family, golf, sports, resting, etc., instead of mowing the lawn). At the bottom of the door hanger will be a coupon offering their tenth (10th) lawn service free, which is the same as a 10% discount.

I have uploaded a template files for the front and back of an 11 x 4 door hanger, The templates are pdf, jpeg, or eps files. The final product can be a pdf, jpeg, or eps file.

Target Market(s)

Neighbors of our existing clients

Industry/Entity Type

Lawn Care

Font styles to use
Serif

Requirements
Must have
• Professional design and art, Short conversational message that relays the following thoughts:
• 1. We mowed your neighbor's lawn today!
• 2. We are in your neighborhood every Tuesday!
• 3. Our lawn service is guaranteed.
• 4. Call to action - Call us today! 555-014-7382
• 5. Of course our contact info, name, phone number, website address.
• 6. Coupon at bottom for "10th lawn service Free!"
Nice to have
• Art work from our website is fine to use, That carries our theme throughout our campaign.
Should not have
• Very wordy. This is basically a billboard, Have very few seconds to grab their attention.

```html
<!DOCTYPE html>
<html lang="en">
<head>
<meta charset="utf-8">
<title>VerdaTurfix Door Hanger</title>
<link rel="stylesheet" href="https://fonts.googleapis.com/css2?family=Montserrat:wght@700;800;900&family=Oswald:wght@500;600&family=Cinzel:wght@400;500&display=swap">
<style>
  :root {
    --bg: #2b2b2b;
    --paper: #ffffff;
    --ink: #000000;
    --red: #e8392a;
    --red-deep: #c92a1d;
    --grass-light: #5fae3c;
    --grass-mid: #3a8a24;
    --grass-dark: #0f240c;
    --text-light: #ffffff;
  }
  * { box-sizing: border-box; margin: 0; padding: 0; }
  html, body { width: 982px; height: 1200px; overflow: hidden; }
  body { background: var(--bg); position: relative; font-family: "Montserrat", sans-serif; color: var(--text-light); }

  .hanger { position: absolute; top: 50px; width: 416px; height: 1100px; background: var(--paper); padding: 12px; }
  .hanger--front { left: 50px; }
  .hanger--back { left: 518px; }
  .hanger__inner { position: relative; width: 392px; height: 1076px; overflow: hidden; background: var(--grass-mid); }

  .header { position: absolute; left: 0; top: 0; width: 100%; height: 68px; background: var(--ink); z-index: 5;
    display: flex; align-items: center; justify-content: center; gap: 14px; font-weight: 800; font-size: 36px; letter-spacing: 1px; }
  .header__icon { width: 38px; height: 38px; }

  .scene { position: absolute; left: 0; top: 68px; width: 100%; height: 810px; }
  .scene--mower { background: linear-gradient(90deg, #b8231a 0%, #e0412f 22%, #8a2a1e 38%, #3f7d27 58%, #5fae3c 78%, #3d8b25 100%); }
  .scene--lawn { background: linear-gradient(170deg, #6fbf45 0%, #4a9a2e 30%, #3b8526 60%, #2f6f1e 100%); }

  .ribbon { position: absolute; width: 320px; height: 58px; background: var(--red); z-index: 4;
    display: flex; flex-direction: column; align-items: center; justify-content: center;
    font-weight: 800; font-size: 17px; line-height: 1.1; text-align: center; letter-spacing: .5px;
    box-shadow: 0 3px 8px rgba(0,0,0,.35); }
  .ribbon--left { left: -87px; top: 113px; transform: rotate(-45deg); }
  .ribbon--right { left: 161px; top: 113px; transform: rotate(45deg); }

  .hole-ring { position: absolute; left: 93px; top: 61px; width: 204px; height: 204px; border-radius: 50%;
    background: radial-gradient(circle, #1d3a16 0%, #0b1608 70%); border: 2px solid var(--paper); z-index: 3; }
  .hole { position: absolute; left: 131px; top: 98px; width: 128px; height: 128px; border-radius: 50%; background: var(--paper); z-index: 6; }

  .panel { position: absolute; border: 2px solid var(--paper);
    background: linear-gradient(180deg, rgba(80,160,50,.95) 0%, rgba(34,80,22,.95) 45%, rgba(10,22,8,.97) 100%);
    text-shadow: 0 2px 4px rgba(0,0,0,.7); font-weight: 800; text-transform: uppercase; }

  .panel--mowed { left: 46px; top: 270px; width: 293px; height: 245px; padding: 22px 0 0 28px; font-size: 34px; line-height: 41px; }
  .tick-badge { display: inline-block; vertical-align: -8px; margin-left: 16px; width: 44px; height: 44px; }
  .panel--day { left: 46px; top: 534px; width: 293px; height: 177px; padding: 20px 0 0 26px; font-size: 33px; line-height: 40px; }
  .panel--day .day { font-size: 47px; line-height: 56px; display: block; }
  .panel--call { left: 46px; top: 731px; width: 293px; height: 112px; padding: 16px 0 0 22px; font-size: 28px; line-height: 34px; }
  .panel--call .phone { font-size: 36px; line-height: 44px; display: block; }

  .panel--slogan { left: 28px; top: 298px; width: 334px; height: 104px; padding: 12px 0 0 34px; font-size: 34px; line-height: 39px; }
  .panel--slogan::before, .panel--slogan::after { content: ""; position: absolute; top: 0; width: 14px; height: 100%; background: var(--red); }
  .panel--slogan::before { left: 0; }
  .panel--slogan::after { right: 0; }

  .panel--services { left: 28px; top: 445px; width: 334px; height: 293px; padding: 18px 0 0 22px; }
  .services__title { font-size: 27px; line-height: 32px; margin-bottom: 6px; }
  .services__list { list-style: none; font-family: "Cinzel", serif; font-weight: 400; font-size: 20px; }
  .services__item { display: flex; align-items: center; gap: 10px; height: 35.5px; }
  .services__tick { width: 28px; height: 28px; flex: none; }

  .contact { position: absolute; left: 46px; top: 764px; font-weight: 800; font-size: 16.5px; text-shadow: 0 2px 3px rgba(0,0,0,.6); }
  .contact__row { display: flex; align-items: center; gap: 12px; height: 32px; }
  .contact__icon { width: 24px; height: 24px; flex: none; }

  .perforation { position: absolute; left: 0; top: 877px; width: 100%; border-top: 2px dashed var(--paper); z-index: 2; }

  .coupon { position: absolute; left: 0; top: 879px; width: 100%; height: 197px;
    background: linear-gradient(90deg, var(--red) 0%, #d8452a 50%, #a5c63a 100%); }
  .coupon__body { position: absolute; left: 14px; top: 13px; width: 364px; height: 170px; overflow: hidden;
    background: linear-gradient(180deg, #1e4a16 0%, #0f2a0c 60%, #143a10 100%);
    font-family: "Oswald", sans-serif; font-weight: 600; text-transform: uppercase; text-shadow: 0 2px 4px rgba(0,0,0,.6); }
  .coupon__body > div { white-space: nowrap; }
  .coupon__lead { position: absolute; left: 20px; top: 14px; font-size: 34px; line-height: 42px; letter-spacing: -0.5px; }
  .coupon__lead sup { font-size: 16px; vertical-align: 16px; margin-right: 4px; }
  .coupon__free { position: absolute; left: 20px; top: 56px; font-size: 76px; line-height: 96px; letter-spacing: 1px; }
  .coupon__with { position: absolute; left: 186px; top: 62px; font-size: 36px; line-height: 44px; }
  .coupon__coupon { position: absolute; left: 186px; top: 104px; font-size: 30px; line-height: 40px; letter-spacing: 8.5px; }

  .coupon__name { position: absolute; left: 0; width: 100%; top: 20px; text-align: center; font-family: "Montserrat", sans-serif; font-weight: 800; font-size: 42px; line-height: 50px; }
  .coupon__phone { position: absolute; left: 0; width: 100%; top: 74px; text-align: center; font-size: 58px; line-height: 70px; }
</style>
</head>
<body>

<section class="hanger hanger--front">
  <div class="hanger__inner">
    <header class="header">VERDATURFIX</header>
    <div class="scene scene--mower" role="img" aria-label="Close-up photo of a red lawn mower on fresh green grass"></div>
    <div class="ribbon ribbon--left"><span>SERVICES</span><span>GUARANTEED!</span></div>
    <div class="hole"></div>

    <div class="panel panel--mowed">We mowed<br>your<br>neighbours<br>lawn<br>today<svg class="tick-badge" viewBox="0 0 44 44"><circle cx="22" cy="22" r="21" fill="#fff"/><path d="M12 23l7 7 13-15" fill="none" stroke="#111" stroke-width="5" stroke-linecap="round" stroke-linejoin="round"/></svg></div>

    <div class="panel panel--day">We’re in the<br>area every<span class="day">Tuesday!</span></div>

    <div class="panel panel--call">Call us today!<span class="phone">555-014-7382</span></div>

    <div class="perforation"></div>
    <div class="coupon">
      <div class="coupon__body">
        <div class="coupon__lead">10<sup>th</sup>lawn service is</div>
        <div class="coupon__free">Free</div>
        <div class="coupon__with">with this</div>
        <div class="coupon__coupon">coupon</div>
      </div>
    </div>
  </div>
</section>

<section class="hanger hanger--back">
  <div class="hanger__inner">
    <header class="header">
      <svg class="header__icon" viewBox="0 0 38 38"><circle cx="19" cy="19" r="19" fill="#fff"/><path d="M13 9c1-1 2-1 3 0l2 4c.5 1 0 2-1 2.5l-1.5 1c1 3 3 5 6 6.5l1-1.5c.5-1 1.5-1.5 2.5-1l4 2c1 1 1 2 0 3l-2 2c-1.5 1.5-4 1.5-7 0-4-2-8-6-10-10-1.5-3-1.5-5.5 0-7z" fill="#000"/></svg>
      555-014-7382
    </header>
    <div class="scene scene--lawn" role="img" aria-label="Photo of a freshly mowed striped green lawn"></div>
    <div class="ribbon ribbon--right"><span>SERVICES</span><span>GUARANTEED!</span></div>
    <div class="hole-ring"></div>
    <div class="hole"></div>

    <div class="panel panel--slogan">Let us do the<br>hard work!</div>

    <div class="panel panel--services">
      <div class="services__title">Our Services</div>
      <ul class="services__list">
        <li class="services__item"><svg class="services__tick" viewBox="0 0 28 28"><circle cx="14" cy="14" r="13" fill="#e8392a" stroke="#fff" stroke-width="1.5"/><path d="M8 14.5l4 4 8-9" fill="none" stroke="#fff" stroke-width="3" stroke-linecap="round" stroke-linejoin="round"/></svg>Lawn Mowing</li>
        <li class="services__item"><svg class="services__tick" viewBox="0 0 28 28"><circle cx="14" cy="14" r="13" fill="#e8392a" stroke="#fff" stroke-width="1.5"/><path d="M8 14.5l4 4 8-9" fill="none" stroke="#fff" stroke-width="3" stroke-linecap="round" stroke-linejoin="round"/></svg>Fertilization</li>
        <li class="services__item"><svg class="services__tick" viewBox="0 0 28 28"><circle cx="14" cy="14" r="13" fill="#e8392a" stroke="#fff" stroke-width="1.5"/><path d="M8 14.5l4 4 8-9" fill="none" stroke="#fff" stroke-width="3" stroke-linecap="round" stroke-linejoin="round"/></svg>Weed-Control</li>
        <li class="services__item"><svg class="services__tick" viewBox="0 0 28 28"><circle cx="14" cy="14" r="13" fill="#e8392a" stroke="#fff" stroke-width="1.5"/><path d="M8 14.5l4 4 8-9" fill="none" stroke="#fff" stroke-width="3" stroke-linecap="round" stroke-linejoin="round"/></svg>Landscape Services</li>
        <li class="services__item"><svg class="services__tick" viewBox="0 0 28 28"><circle cx="14" cy="14" r="13" fill="#e8392a" stroke="#fff" stroke-width="1.5"/><path d="M8 14.5l4 4 8-9" fill="none" stroke="#fff" stroke-width="3" stroke-linecap="round" stroke-linejoin="round"/></svg>Sprinkler Repair</li>
        <li class="services__item"><svg class="services__tick" viewBox="0 0 28 28"><circle cx="14" cy="14" r="13" fill="#e8392a" stroke="#fff" stroke-width="1.5"/><path d="M8 14.5l4 4 8-9" fill="none" stroke="#fff" stroke-width="3" stroke-linecap="round" stroke-linejoin="round"/></svg>Landscape Lighting</li>
      </ul>
    </div>

    <div class="contact">
      <div class="contact__row"><svg class="contact__icon" viewBox="0 0 24 24"><circle cx="12" cy="12" r="12" fill="#fff"/><path d="M8 5.5c.6-.6 1.3-.6 1.8 0l1.3 2.5c.3.6 0 1.2-.6 1.5l-.9.6c.6 1.8 1.8 3 3.6 3.9l.6-.9c.3-.6.9-.9 1.5-.6l2.5 1.2c.6.6.6 1.2 0 1.8l-1.2 1.2c-.9.9-2.4.9-4.2 0-2.4-1.2-4.8-3.6-6-6-.9-1.8-.9-3.3 0-4.2z" fill="#000"/></svg>555-014-7382</div>
      <div class="contact__row"><svg class="contact__icon" viewBox="0 0 24 24" fill="none" stroke="#fff" stroke-width="1.8"><circle cx="12" cy="12" r="10.5"/><ellipse cx="12" cy="12" rx="4.5" ry="10.5"/><path d="M1.5 12h21M3.5 6.5h17M3.5 17.5h17"/></svg>WWW.VERDATURFIX.NET</div>
      <div class="contact__row"><svg class="contact__icon" viewBox="0 0 24 24"><circle cx="12" cy="12" r="12" fill="#fff"/><rect x="5.5" y="7.5" width="13" height="9" rx="1" fill="none" stroke="#000" stroke-width="1.6"/><path d="M5.5 8l6.5 5 6.5-5" fill="none" stroke="#000" stroke-width="1.6"/></svg>SERVICE@VERDATURFIX.NET</div>
    </div>

    <div class="perforation"></div>
    <div class="coupon">
      <div class="coupon__body">
        <div class="coupon__name">VERDATURFIX</div>
        <div class="coupon__phone">555-014-7382</div>
      </div>
    </div>
  </div>
</section>

</body>
</html>
```